The Lantern Pact a non-fiction book on mindfulness COVER design needed

A non-fiction book about active mindfulness.
The Lantern Pact includes 21 different daily 'dares' which are action based activities to generate positive mindfulness - to become more contented with life.
Based on the teeaching of the New Thought movements of the early 20th century, think The Hollow, Climb and Gather Plenty.
The book is positive and uplifting. It fits into the self-help / spiritual / health segments. It skews female 40 to 50 year olds.
Think fresh colours like a bold orange or bright green.
What needs to be on the cover:
TITLE: The Lantern Pact
AUTHOR: Marcus Tindall
BLURB: Get clarity, focus, and a new zest for life by following The Lantern Pact for just 21 days.
Target Market(s)
Women 40-50 english speaking
Industry/Entity Type
Self-help / Health

```html
<!DOCTYPE html>
<html lang="en">
<head>
<meta charset="utf-8">
<title>The Lantern Pact — Cover Spread</title>
<link href="https://fonts.googleapis.com/css2?family=Montserrat:wght@300;400;600;700;800&display=swap" rel="stylesheet">
<style>
  :root {
    --teal: #07a78a;
    --teal-deep: #05957b;
    --paper: #ffffff;
    --paper-shade: #f1f1f1;
    --ink: #1a1a1a;
  }
  * { margin: 0; padding: 0; box-sizing: border-box; }
  html, body { width: 1200px; height: 857px; overflow: hidden; }
  body {
    background: var(--teal);
    font-family: "Montserrat", sans-serif;
    color: var(--ink);
    position: relative;
  }
  .cover-panel {
    position: absolute;
    top: 118px;
    height: 617px;
    background: linear-gradient(180deg, var(--paper) 0%, var(--paper-shade) 100%);
    overflow: hidden;
  }

  /* Back cover */
  .back-cover { left: 89px; width: 420px; }
  .back-cover .ring-field {
    position: absolute; left: 0; top: 0; width: 420px; height: 210px;
  }
  .back-title {
    position: absolute; left: 22px; top: 100px;
    font-weight: 800; font-size: 34px; letter-spacing: -1.2px;
    color: var(--teal); line-height: 1; white-space: nowrap;
  }
  .back-copy {
    position: absolute; left: 25px; top: 182px;
    font-size: 17px; line-height: 18.3px; font-weight: 400;
  }
  .back-copy strong { font-weight: 700; }
  .back-footnote {
    position: absolute; left: 20px; top: 497px;
    font-size: 11.5px; font-weight: 700;
  }

  /* Spine */
  .spine { left: 563px; width: 69px; }
  .spine-title {
    position: absolute; left: 50%; top: 40px;
    writing-mode: vertical-rl; transform: translateX(-50%);
    white-space: nowrap;
    font-weight: 800; font-size: 34px; letter-spacing: -1px;
    color: var(--teal); line-height: 1;
  }
  .spine-author {
    position: absolute; left: 50%; top: 426px;
    writing-mode: vertical-rl; transform: translateX(-50%);
    font-weight: 300; font-size: 18px; letter-spacing: 0.5px;
    white-space: nowrap; line-height: 1;
  }

  /* Front cover */
  .front-cover { left: 677px; width: 420px; }
  .front-art {
    position: absolute; left: 0; top: 220px; width: 320px; height: 397px;
    z-index: 1;
  }
  .front-title {
    position: absolute; left: 16px; top: 42px; z-index: 2;
    color: var(--teal); font-weight: 800; line-height: 0.86;
    letter-spacing: -2px; white-space: nowrap;
  }
  .front-title .title-small { display: block; font-size: 52px; }
  .front-title .title-large { display: block; font-size: 128px; letter-spacing: -5px; }
  .front-tagline {
    position: absolute; right: 23px; top: 314px; z-index: 2;
    text-align: right; font-weight: 700; font-size: 11.5px;
    line-height: 17.5px; text-transform: uppercase; white-space: nowrap;
  }
  .front-tagline .accent { color: var(--teal); }
  .front-tagline .big-number { font-size: 17px; font-weight: 700; }
  .front-author {
    position: absolute; right: 24px; top: 504px; z-index: 2;
    text-align: right; font-weight: 300; font-size: 36px;
    line-height: 37px;
  }
</style>
</head>
<body>

  <section class="cover-panel back-cover">
    <svg class="ring-field" role="img" aria-label="Concentric contour-ring pattern radiating from the top edge" viewBox="0 0 420 210">
      <defs>
        <radialGradient id="backRings" cx="0.5" cy="0" r="0.75">
          <stop offset="0" stop-color="#e4e7e6"/>
          <stop offset="1" stop-color="#ffffff" stop-opacity="0"/>
        </radialGradient>
      </defs>
      <rect width="420" height="210" fill="url(#backRings)"/>
    </svg>
    <h2 class="back-title">THE LANTERN PACT</h2>
    <p class="back-copy">
      <strong>Lorem</strong> ipsum Lorem ipsum<br>
      Lorem ipsum Lorem ipsum<br>
      Lorem ipsum Lorem ipsum<br>
      Lorem ipsum Lorem ipsum<br>
      Lorem ipsum Lorem ipsum<br>
      Lorem ipsum Lorem ipsum<br>
      Lorem ipsum Lorem ipsum<br>
      Lorem ipsum Lorem ipsum<br>
      Lorem ipsum Lorem ipsum<br>
      Lorem ipsum Lorem ipsum<br>
      Lorem ipsum Lorem ipsum<br>
      Lorem ipsum Lorem ipsum <strong>.</strong>
    </p>
    <p class="back-footnote">Lorem ipsum Lorem ipsum Lorem ipsum .</p>
  </section>

  <section class="cover-panel spine">
    <span class="spine-title">THE LANTERN PACT</span>
    <span class="spine-author">MARCUS TINDALL</span>
  </section>

  <section class="cover-panel front-cover">
    <svg class="front-art" role="img" aria-label="Silhouette of a standing woman surrounded by rippling contour rings" viewBox="0 0 320 397">
      <defs>
        <radialGradient id="frontRings" cx="0.35" cy="0.55" r="0.7">
          <stop offset="0" stop-color="#dfe3e2"/>
          <stop offset="1" stop-color="#ffffff" stop-opacity="0"/>
        </radialGradient>
      </defs>
      <rect width="320" height="397" fill="url(#frontRings)"/>
      <path d="M49 397 V220 Q49 124 118 124 Q187 124 187 220 V397 Z" fill="var(--teal)"/>
    </svg>
    <h1 class="front-title">
      <span class="title-small">THE LANTERN</span>
      <span class="title-large">PACT</span>
    </h1>
    <p class="front-tagline">
      Get clarity,<br>
      focus, and a new<br>
      zest for life by following<br>
      <span class="accent">The Lantern Pact</span><br>
      for just <span class="big-number">21</span> days.
    </p>
    <p class="front-author">MARCUS<br>TINDALL</p>
  </section>

</body>
</html>
```